A sustainable tourism website

We are a travel/tourism company. We have developed a platform that enables organizers of sustainable theme vacations to publish and make their vacations bookable via our platform. By theme vacations, we mean vacations in categories such as Wellness, Surfing, Culinary, Martial arts, etc. We already have separate websites for each of these categories. This new website you will design is about a parent site where we provide general summary information about these individual sites and link to them. The site would be hosted on the domain veloramix.com. Besides information about the individual sites, we also need a menu for About Us, Products and Our Climate Pledge. We also need the following at the home page:
1. A section that contain our last tweets in a twitter lightbox.
2. Summary and links to of our last few blogs.
3. A video as banner or an image. We would prefer a video though.
We already have a logo and have uploaded it. Please make sure your design conforms with our logo style and colors.
NB: We are looking for something more than the standard site you see everywhere. The winning design is a design that stands out and has a WOW effect. And when your design is selected, we intend to work with you further for the completion of the whole site.

Target Market(s)

Sustainable tourism

Number of Pages Required

1 page

Requirements
Must have
• Conform to logo design and colors.
Site must be unique, slick and stand out.
Must have a climate/sustainability blended with tourism look.
Nice to have
• Video as banner.

```html
<!DOCTYPE html>
<html lang="en">
<head>
<meta charset="utf-8">
<title>veloramix – Sustainable Theme Vacations</title>
<link href="https://fonts.googleapis.com/css2?family=Poppins:wght@300;400;500;600;700&display=swap" rel="stylesheet">
<style>
:root{
  --orange:#f7901e;
  --orange-dark:#e8811a;
  --blue:#4ca7ec;
  --ink:#1f1f1f;
  --text:#444;
  --muted:#9a9a9a;
  --line:#dcdcdc;
  --grey-bg:#f1f1f1;
  --white:#fff;
}
*{box-sizing:border-box;margin:0;padding:0}
html,body{width:1200px;height:3748px;overflow:hidden}
body{font-family:'Poppins',sans-serif;color:var(--ink);background:var(--white);position:relative}
.abs{position:absolute}
a{color:inherit;text-decoration:none}

/* photo placeholders: soft layered gradients in each scene's main tones */
.photo{position:relative;overflow:hidden}
.ph-pool{background:radial-gradient(ellipse 45% 55% at 30% 60%,#f2c9a8 0%,rgba(242,201,168,0) 70%),radial-gradient(ellipse 35% 50% at 68% 50%,#e9b99a 0%,rgba(233,185,154,0) 70%),linear-gradient(180deg,#cfe6f2 0%,#7cc6ee 22%,#3a9bdc 65%,#2b86c9 100%)}
.ph-sunset{background:radial-gradient(ellipse 40% 45% at 62% 30%,#fff4c8 0%,rgba(255,236,170,0) 70%),radial-gradient(ellipse 18% 45% at 45% 55%,#5b3a1e 0%,rgba(91,58,30,0) 75%),linear-gradient(180deg,#f7d56a 0%,#efb23d 45%,#c7832a 75%,#7d5220 100%)}
.ph-surf{background:radial-gradient(ellipse 30% 22% at 55% 42%,#ffe6a8 0%,rgba(255,230,168,0) 70%),radial-gradient(ellipse 22% 60% at 45% 55%,#2a2320 0%,rgba(42,35,32,0) 70%),linear-gradient(180deg,#f0b764 0%,#e39a4a 40%,#8f6b52 62%,#3e3530 100%)}
.ph-sea{background:radial-gradient(ellipse 30% 40% at 45% 45%,#f0c9a2 0%,rgba(240,201,162,0) 70%),radial-gradient(ellipse 60% 30% at 50% 85%,#e8f3f4 0%,rgba(232,243,244,0) 70%),linear-gradient(180deg,#a7bcc6 0%,#6f97a8 35%,#3b7891 70%,#2d6379 100%)}
.ph-dojo{background:radial-gradient(ellipse 70% 40% at 50% 55%,#f4f4f4 0%,rgba(244,244,244,0) 75%),linear-gradient(180deg,#d9d6d1 0%,#e8e6e2 30%,#c9cdd6 55%,#3f73c0 80%,#2f5fa8 100%)}
.ph-chef{background:radial-gradient(ellipse 70% 35% at 50% 25%,#f7f6f3 0%,rgba(247,246,243,0) 75%),radial-gradient(ellipse 30% 20% at 55% 75%,#d85a3b 0%,rgba(216,90,59,0) 70%),linear-gradient(180deg,#d8d2cb 0%,#b8a99b 45%,#6f5648 75%,#3b2c25 100%)}
.ph-hike{background:radial-gradient(ellipse 40% 35% at 35% 20%,#7fb5c8 0%,rgba(127,181,200,0) 75%),radial-gradient(ellipse 40% 45% at 60% 55%,#d9a27e 0%,rgba(217,162,126,0) 70%),linear-gradient(160deg,#5f94a8 0%,#4f7f6a 30%,#53733d 60%,#6c6a3e 85%,#8b7a5a 100%)}
.ph-jeep{background:radial-gradient(ellipse 35% 30% at 55% 65%,#c93a33 0%,rgba(201,58,51,0) 70%),linear-gradient(180deg,#8fc6ea 0%,#bcdcee 40%,#c9b79c 62%,#857265 80%,#5d5550 100%)}
.ph-splash{background:radial-gradient(ellipse 30% 40% at 40% 50%,#d6a27c 0%,rgba(214,162,124,0) 70%),radial-gradient(ellipse 50% 40% at 30% 20%,#e8f1f4 0%,rgba(232,241,244,0) 70%),linear-gradient(180deg,#8db4c3 0%,#5b8ea5 50%,#2f5d75 100%)}
.ph-yoga{background:radial-gradient(ellipse 40% 30% at 50% 35%,#f1d4a0 0%,rgba(241,212,160,0) 70%),radial-gradient(ellipse 12% 45% at 32% 60%,#2d2e38 0%,rgba(45,46,56,0) 75%),linear-gradient(180deg,#8793a0 0%,#b8a489 50%,#6e6658 100%)}
.ph-wave{background:radial-gradient(ellipse 30% 25% at 45% 30%,#e5b79a 0%,rgba(229,183,154,0) 70%),radial-gradient(ellipse 35% 30% at 80% 65%,#c9925a 0%,rgba(201,146,90,0) 70%),linear-gradient(180deg,#1f6f80 0%,#3a8d9b 40%,#7db2b5 70%,#bcd3cf 100%)}
.ph-salad{background:radial-gradient(ellipse 35% 30% at 50% 45%,#e9e3d3 0%,rgba(233,227,211,0) 70%),radial-gradient(ellipse 20% 15% at 48% 47%,#c55a34 0%,rgba(197,90,52,0) 75%),linear-gradient(180deg,#2a2a2a 0%,#4c4a47 40%,#8d8678 70%,#3a3836 100%)}
.ph-karate{background:radial-gradient(ellipse 45% 55% at 50% 45%,#f3f2ef 0%,rgba(243,242,239,0) 70%),radial-gradient(ellipse 15% 12% at 50% 20%,#d8b499 0%,rgba(216,180,153,0) 75%),linear-gradient(180deg,#6f6d6a 0%,#9a9895 50%,#3f3c3a 100%)}

/* header */
.site-header{position:absolute;left:0;top:0;width:1200px;height:81px;background:var(--white)}
.brand{position:absolute;left:125px;top:20px;display:flex;align-items:center;gap:8px;font-size:33px;font-weight:300;color:var(--orange);letter-spacing:.5px}
.brand-dot{width:12px;height:12px;border-radius:50%;background:var(--orange)}
.top-contact{position:absolute;right:138px;top:11px;display:flex;align-items:center;gap:22px;font-size:13px;color:var(--ink)}
.top-contact span{display:flex;align-items:center;gap:7px}
.social{display:flex;gap:9px}
.social i{display:block;width:25px;height:25px;border-radius:50%;background:#4a4a4a}
.social i.on{background:var(--orange)}
.main-nav{position:absolute;right:128px;top:49px;display:flex;gap:30px;font-size:14.5px;font-weight:400}
.main-nav a.active{border-bottom:2px solid var(--orange)}

/* hero */
.hero{position:absolute;left:0;top:81px;width:1200px;height:498px;
  background:radial-gradient(ellipse 14% 42% at 28% 38%,#2f5b4d 0%,rgba(47,91,77,0) 75%),radial-gradient(ellipse 12% 45% at 64% 40%,#e9e2d4 0%,rgba(233,226,212,0) 75%),radial-gradient(ellipse 50% 30% at 20% 10%,#4d6b3a 0%,rgba(77,107,58,0) 75%),linear-gradient(180deg,#5f7d4a 0%,#8fa06c 25%,#d3c29d 50%,#e6d6b8 72%,#c7b390 100%)}
.hero-sea{position:absolute;right:0;top:120px;width:560px;height:300px;background:linear-gradient(100deg,rgba(60,160,165,0) 0%,rgba(56,160,165,.55) 45%,rgba(40,140,150,.85) 100%)}
.hero-shade{position:absolute;inset:0;background:linear-gradient(180deg,rgba(0,0,0,.05),rgba(0,0,0,.18))}
.hero-copy{position:absolute;left:0;top:188px;width:1200px;text-align:center;color:var(--white)}
.hero-copy h1{font-size:35px;font-weight:600;color:var(--orange);line-height:1.2}
.hero-copy p{font-size:14px;line-height:19px;margin-top:6px}
.btn-pill{display:inline-block;border-radius:16px;font-size:10.5px;text-transform:uppercase;text-align:center}
.hero .btn-pill{margin-top:17px;width:116px;height:29px;line-height:29px;background:var(--white);color:var(--ink)}
.dots{position:absolute;left:565px;top:465px;display:flex;gap:8px}
.dots i{display:block;width:9px;height:9px;border:1px solid var(--white);border-radius:50%}
.dots i.on{background:var(--orange);border-color:var(--orange)}

/* headings */
.sec-title{position:absolute;left:0;width:1200px;text-align:center;font-size:22px;font-weight:600;text-transform:uppercase}
.sec-title span{border-bottom:2.5px solid var(--ink);padding-bottom:1px}
.btn-outline{position:absolute;left:50%;transform:translateX(-50%);width:100px;height:27px;line-height:25px;border:1px solid #888;border-radius:14px;font-size:10.5px;text-align:center;text-transform:uppercase;background:var(--white)}

/* about */
.about-text{position:absolute;left:134px;top:686px;width:932px;text-align:center;font-size:12.5px;line-height:22px;color:var(--text)}

/* categories */
.categories{position:absolute;left:0;top:860px;width:1200px;height:353px;background:var(--orange)}
.cat-row{position:absolute;left:0;top:90px;width:1200px;height:173px;display:flex;gap:1px}
.cat{position:relative;flex:1;overflow:hidden}
.cat::after{content:"";position:absolute;inset:0;background:linear-gradient(180deg,rgba(0,0,0,0) 35%,rgba(0,0,0,.65) 100%)}
.cat-text{position:absolute;left:15px;bottom:12px;z-index:1;color:var(--white)}
.cat-text h3{font-size:17px;font-weight:600;color:var(--orange);line-height:22px}
.cat-text p{font-size:11.5px}
.categories .btn-outline{top:296px;background:transparent;border-color:var(--white);color:var(--white)}

/* packages */
.pkg{position:absolute;width:299px;height:402px;background:var(--white);box-shadow:0 2px 10px rgba(0,0,0,.09)}
.pkg-img{height:205px}
.pkg h4{position:absolute;left:23px;top:222px;width:236px;font-size:14px;font-weight:600;line-height:22px}
.pkg .desc{position:absolute;left:23px;top:280px;width:236px;font-size:12px;line-height:20px;color:var(--muted)}
.pkg .rev{position:absolute;left:23px;top:345px;font-size:10.5px;color:var(--muted)}
.pkg .stars{position:absolute;left:23px;top:359px;font-size:14px;color:var(--orange);letter-spacing:2px}
.pkg .old{position:absolute;right:23px;top:345px;font-size:11px;color:var(--muted);text-decoration:line-through}
.pkg .price{position:absolute;right:23px;top:362px;font-size:16px;font-weight:600;color:var(--orange)}

/* blogs */
.blogs{position:absolute;left:0;top:2278px;width:1200px;height:648px;background:var(--grey-bg)}
.blog{position:absolute}
.blog h5{font-size:13px;font-weight:400;line-height:21px;margin-top:14px}
.blog.big h5{font-size:16px;line-height:22px;margin-top:20px}
.blog-meta{display:flex;align-items:center;gap:14px;margin-top:10px;font-size:11px}
.blog-meta .date{display:flex;align-items:center;gap:8px}
.blog-meta .btn-pill{width:100px;height:26px;line-height:24px;border:1px solid #888;background:var(--white)}
.blog-meta .btn-pill.hot{background:var(--orange);border-color:var(--orange);color:var(--white)}

/* social feed */
.feed{position:absolute;left:0;top:2926px;width:1200px;height:150px;background:var(--blue);color:var(--white)}
.feed-label{position:absolute;left:145px;top:45px;width:120px;text-align:center;font-size:14px}
.feed-label i{display:block;width:36px;height:36px;margin:0 auto 10px;border-radius:8px;background:var(--white)}
.tweet{position:absolute;top:35px;width:350px;font-size:12.5px;line-height:19px}
.tweet small{display:block;margin-top:8px;font-size:11.5px;color:rgba(255,255,255,.6)}
.feed-divider{position:absolute;left:691px;top:35px;width:1px;height:76px;background:rgba(255,255,255,.45)}

/* inquiry */
.inquiry-bg{position:absolute;left:0;top:3396px;width:1200px;height:352px;background:var(--grey-bg)}
.inquiry{position:absolute;left:163px;top:3149px;width:874px;height:371px;background:var(--white);box-shadow:0 2px 14px rgba(0,0,0,.08)}
.inquiry h2{position:absolute;left:38px;top:30px;font-size:20px;font-weight:600;border-bottom:2px solid var(--ink);line-height:26px}
.field{position:absolute;height:41px;border:1px solid var(--line);font-size:12.5px;color:var(--muted);padding:11px 15px}
.submit{position:absolute;left:39px;top:303px;width:98px;height:35px;line-height:35px;background:var(--orange);color:var(--white);text-align:center;font-size:12.5px}
.contact-info{position:absolute;left:580px;top:0;width:294px;height:371px;background:var(--orange);color:var(--white)}
.contact-info h2{position:absolute;left:31px;top:26px;font-size:22px;font-weight:500;border:none}
.ci{position:absolute;left:70px;font-size:12.5px;line-height:17px}
.ci small{display:block;font-size:11.5px;color:rgba(255,255,255,.75)}
.ci svg{position:absolute;left:-34px;top:4px}
.contact-info .social{position:absolute;left:35px;top:311px;gap:19px}
.contact-info .social i{background:var(--white);opacity:.9}

/* footer */
.footer-brand{position:absolute;left:0;top:3568px;width:1200px;display:flex;justify-content:center;align-items:center;gap:8px;font-size:31px;font-weight:300;color:var(--orange)}
.footer-nav{position:absolute;left:0;top:3637px;width:1200px;display:flex;justify-content:center;gap:40px;font-size:14px;font-weight:400}
.footer-nav a.active{border-bottom:2px solid var(--orange)}
.copyright{position:absolute;left:0;top:3670px;width:1200px;text-align:center;font-size:11.5px;color:#666}
</style>
</head>
<body>

<header class="site-header">
  <div class="brand">veloramix<span class="brand-dot"></span></div>
  <div class="top-contact">
    <span><svg width="18" height="13" viewBox="0 0 18 13"><rect x="1" y="1" width="16" height="11" fill="none" stroke="#f7901e" stroke-width="1.8"/><path d="M1 1l8 6 8-6" fill="none" stroke="#f7901e" stroke-width="1.8"/></svg>hello@veloramix.com</span>
    <span><svg width="14" height="14" viewBox="0 0 24 24"><path d="M6.6 10.8a15 15 0 006.6 6.6l2.2-2.2a1 1 0 011-.25 11.4 11.4 0 003.6.57 1 1 0 011 1V20a1 1 0 01-1 1A17 17 0 013 4a1 1 0 011-1h3.5a1 1 0 011 1 11.4 11.4 0 00.57 3.6 1 1 0 01-.25 1z" fill="#f7901e"/></svg>+00 12 345 678</span>
    <div class="social" aria-label="Social links"><i class="on"></i><i></i><i></i></div>
  </div>
  <nav class="main-nav">
    <a class="active" href="#">Home</a><a href="#">About Us</a><a href="#">Products</a><a href="#">Our Climate Pledge</a><a href="#">blogs</a><a href="#">Contact Us</a>
  </nav>
</header>

<section class="hero">
  <div role="img" aria-label="Video banner: family walking along a tropical beach carrying beach toys" class="abs" style="inset:0">
    <div class="hero-sea"></div>
    <div class="hero-shade"></div>
  </div>
  <div class="hero-copy">
    <h1>The Best Tour Experience</h1>
    <p>Lorem Ipsum is simply dummy text of the printing and<br>typesetting industry.</p>
    <a class="btn-pill" href="#">Read More</a>
  </div>
  <div class="dots"><i></i><i class="on"></i><i></i><i></i></div>
</section>

<section class="about">
  <h2 class="sec-title" style="top:627px"><span>About Us</span></h2>
  <p class="about-text">Lorem Ipsum is simply dummy text of the printing and typesetting industry. Lorem Ipsum has been the industry's standard dummy text ever since the 1500s, when an unknown printer took a galley of type and scrambled it to make a type specimen book. It has survived not only five centuries, but also the leap into electronic typesetting, remaining essentially unchanged...</p>
  <a class="btn-outline" href="#" style="top:778px;width:122px">Click to more</a>
</section>

<section class="categories">
  <h2 class="sec-title" style="top:32px"><span>Categories</span></h2>
  <div class="cat-row">
    <div class="cat ph-yoga" role="img" aria-label="Wellness photo: person doing yoga at sunset"><div class="cat-text"><h3>Wellness</h3><p>Lorem Ipsum is simply dummy text...</p></div></div>
    <div class="cat ph-wave" role="img" aria-label="Surfing photo: surfer riding a wave"><div class="cat-text"><h3>Surfing</h3><p>Lorem Ipsum is simply dummy text...</p></div></div>
    <div class="cat ph-salad" role="img" aria-label="Culinary photo: chef presenting a fresh salad"><div class="cat-text"><h3>Culinary</h3><p>Lorem Ipsum is simply dummy text...</p></div></div>
    <div class="cat ph-karate" role="img" aria-label="Martial arts photo: practitioner in a white uniform"><div class="cat-text"><h3>Martial arts</h3><p>Lorem Ipsum is simply dummy text...</p></div></div>
  </div>
  <a class="btn-outline" href="#">View All</a>
</section>

<section class="packages">
  <h2 class="sec-title" style="top:1261px"><span>Our Vacation Packages</span></h2>

  <article class="pkg" style="left:127px;top:1327px"><div class="pkg-img ph-pool" role="img" aria-label="Family playing in a swimming pool"></div><h4>Lorem Ipsum is simply dummy text industry.</h4><p class="desc">Lorem Ipsum is simply dummy text of the printing and typesetting...</p><span class="rev">(1 Review)</span><span class="stars">★★★★★</span><span class="old">$625.00</span><span class="price">$562,50</span></article>
  <article class="pkg" style="left:450px;top:1327px"><div class="pkg-img ph-sunset" role="img" aria-label="Woman raising arms in a golden sunset meadow"></div><h4>Lorem Ipsum is simply dummy text industry.</h4><p class="desc">Lorem Ipsum is simply dummy text of the printing and typesetting...</p><span class="rev">(1 Review)</span><span class="stars">★★★★★</span><span class="old">$625.00</span><span class="price">$562,50</span></article>
  <article class="pkg" style="left:774px;top:1327px"><div class="pkg-img ph-surf" role="img" aria-label="Surfers with boards on a beach at sunset"></div><h4>Lorem Ipsum is simply dummy text industry.</h4><p class="desc">Lorem Ipsum is simply dummy text of the printing and typesetting...</p><span class="rev">(1 Review)</span><span class="stars">★★★★★</span><span class="old">$625.00</span><span class="price">$562,50</span></article>

  <article class="pkg" style="left:127px;top:1754px"><div class="pkg-img ph-sea" role="img" aria-label="Woman swimming in the sea"></div><h4>Lorem Ipsum is simply dummy text industry.</h4><p class="desc">Lorem Ipsum is simply dummy text of the printing and typesetting...</p><span class="rev">(1 Review)</span><span class="stars">★★★★★</span><span class="old">$625.00</span><span class="price">$562,50</span></article>
  <article class="pkg" style="left:450px;top:1754px"><div class="pkg-img ph-dojo" role="img" aria-label="Children in martial arts uniforms sitting on a mat"></div><h4>Lorem Ipsum is simply dummy text industry.</h4><p class="desc">Lorem Ipsum is simply dummy text of the printing and typesetting...</p><span class="rev">(1 Review)</span><span class="stars">★★★★★</span><span class="old">$625.00</span><span class="price">$562,50</span></article>
  <article class="pkg" style="left:774px;top:1754px"><div class="pkg-img ph-chef" role="img" aria-label="Children in chef hats cooking together"></div><h4>Lorem Ipsum is simply dummy text industry.</h4><p class="desc">Lorem Ipsum is simply dummy text of the printing and typesetting...</p><span class="rev">(1 Review)</span><span class="stars">★★★★★</span><span class="old">$625.00</span><span class="price">$562,50</span></article>

  <a class="btn-outline" href="#" style="top:2196px">View All</a>
</section>

<section class="blogs">
  <h2 class="sec-title" style="top:48px"><span>Blogs</span></h2>

  <article class="blog big" style="left:127px;top:113px;width:376px">
    <div class="ph-hike" role="img" aria-label="Smiling traveller in sunglasses above a bay" style="height:380px"></div>
    <h5>10 Travel Blog Post Ideas For Your<br>Weekend Trip</h5>
    <div class="blog-meta"><span class="date"><svg width="13" height="13" viewBox="0 0 13 13"><rect x="1" y="2" width="11" height="10" fill="none" stroke="#f7901e" stroke-width="1.4"/><path d="M1 5h11M4 0v3M9 0v3" stroke="#f7901e" stroke-width="1.4"/></svg>30 Nov, 2020</span><a class="btn-pill" href="#">Read More</a></div>
  </article>

  <article class="blog" style="left:527px;top:113px;width:262px">
    <div class="ph-jeep" role="img" aria-label="Friends cheering on an open jeep on a road" style="height:142px"></div>
    <h5>10 Travel Blog Post Ideas For Your<br>Weekend Trip</h5>
    <div class="blog-meta"><span class="date"><svg width="13" height="13" viewBox="0 0 13 13"><rect x="1" y="2" width="11" height="10" fill="none" stroke="#f7901e" stroke-width="1.4"/><path d="M1 5h11M4 0v3M9 0v3" stroke="#f7901e" stroke-width="1.4"/></svg>30 Nov, 2020</span><a class="btn-pill hot" href="#">Read More</a></div>
  </article>
  <article class="blog" style="left:812px;top:113px;width:262px">
    <div class="ph-pool" role="img" aria-label="Family playing in a swimming pool" style="height:142px"></div>
    <h5>14 Things To See And Do When Visiting<br>Kyoto</h5>
    <div class="blog-meta"><span class="date"><svg width="13" height="13" viewBox="0 0 13 13"><rect x="1" y="2" width="11" height="10" fill="none" stroke="#f7901e" stroke-width="1.4"/><path d="M1 5h11M4 0v3M9 0v3" stroke="#f7901e" stroke-width="1.4"/></svg>30 Nov, 2020</span><a class="btn-pill" href="#">Read More</a></div>
  </article>
  <article class="blog" style="left:527px;top:365px;width:262px">
    <div class="ph-sunset" role="img" aria-label="Woman raising arms in a golden sunset meadow" style="height:141px"></div>
    <h5>Backpacking Laos: A Full Travel Guide<br>for You</h5>
    <div class="blog-meta"><span class="date"><svg width="13" height="13" viewBox="0 0 13 13"><rect x="1" y="2" width="11" height="10" fill="none" stroke="#f7901e" stroke-width="1.4"/><path d="M1 5h11M4 0v3M9 0v3" stroke="#f7901e" stroke-width="1.4"/></svg>30 Nov, 2020</span><a class="btn-pill" href="#">Read More</a></div>
  </article>
  <article class="blog" style="left:812px;top:365px;width:262px">
    <div class="ph-splash" role="img" aria-label="Father and child splashing in the sea" style="height:141px"></div>
    <h5>10 Travel Blog Post Ideas For Your<br>Weekend Trip</h5>
    <div class="blog-meta"><span class="date"><svg width="13" height="13" viewBox="0 0 13 13"><rect x="1" y="2" width="11" height="10" fill="none" stroke="#f7901e" stroke-width="1.4"/><path d="M1 5h11M4 0v3M9 0v3" stroke="#f7901e" stroke-width="1.4"/></svg>30 Nov, 2020</span><a class="btn-pill" href="#">Read More</a></div>
  </article>
</section>

<section class="feed">
  <div class="feed-label"><i></i>Social Feed</div>
  <p class="tweet" style="left:318px">@mirolanhelp Hi @mirolanhelp , can you please submit a ticket at https://lnk.example/ab12cd and one of our support agent... https://lnk.example/ef34gh<small>1 day ago</small></p>
  <div class="feed-divider"></div>
  <p class="tweet" style="left:726px">@mirolanhelp Hi @mirolanhelp , can you please submit a ticket at https://lnk.example/ab12cd and one of our support agent... https://lnk.example/ef34gh<small>5 months ago</small></p>
</section>

<div class="inquiry-bg"></div>
<section class="inquiry">
  <h2>Quick Inquiry</h2>
  <div class="field" style="left:39px;top:79px;width:246px">Name</div>
  <div class="field" style="left:298px;top:79px;width:246px">Company / Organisation</div>
  <div class="field" style="left:39px;top:138px;width:246px">Phone</div>
  <div class="field" style="left:298px;top:138px;width:246px">Email</div>
  <div class="field" style="left:39px;top:196px;width:505px;height:80px">Message</div>
  <a class="submit" href="#">SUBMIT</a>

  <div class="contact-info">
    <h2>Contact Info</h2>
    <div class="ci" style="top:82px"><svg width="16" height="20" viewBox="0 0 16 20"><path d="M8 1a6.5 6.5 0 00-6.5 6.5C1.5 12 8 19 8 19s6.5-7 6.5-11.5A6.5 6.5 0 008 1z" fill="none" stroke="#fff" stroke-width="1.5"/><circle cx="8" cy="7.5" r="2.3" fill="none" stroke="#fff" stroke-width="1.5"/></svg><small>Location</small>Example Lane 4<br>Riverton RV 10001<br>Eastland</div>
    <div class="ci" style="top:175px"><svg width="16" height="16" viewBox="0 0 24 24"><path d="M6.6 10.8a15 15 0 006.6 6.6l2.2-2.2a1 1 0 011-.25 11.4 11.4 0 003.6.57 1 1 0 011 1V20a1 1 0 01-1 1A17 17 0 013 4a1 1 0 011-1h3.5a1 1 0 011 1 11.4 11.4 0 00.57 3.6 1 1 0 01-.25 1z" fill="none" stroke="#fff" stroke-width="1.6"/></svg><small>Call Us</small>+00 12 345 678</div>
    <div class="ci" style="top:235px"><svg width="18" height="13" viewBox="0 0 18 13"><rect x="1" y="1" width="16" height="11" fill="none" stroke="#fff" stroke-width="1.5"/><path d="M1 1l8 6 8-6" fill="none" stroke="#fff" stroke-width="1.5"/></svg><small>Email</small>hello@veloramix.com</div>
    <div class="social" aria-label="Social links"><i></i><i></i><i></i></div>
  </div>
</section>

<footer>
  <div class="footer-brand">veloramix<span class="brand-dot"></span></div>
  <nav class="footer-nav"><a class="active" href="#">Home</a><a href="#">About Us</a><a href="#">Products</a><a href="#">Our Climate Pledge</a><a href="#">Blogs</a><a href="#">Contact Us</a></nav>
  <p class="copyright">Copyright © 2020 veloramix. All Rights Reserved</p>
</footer>

</body>
</html>
```